Upscale Children's Boutique Needs a PSD Web Design

We need a PSD web design for an online children's boutique called 'Mavoret'. We specialize in special occasion wear for infants. Our apparel products are typically selected for christening & baptisms, birthdays, holidays and weddings. We would like to see designs that compliment our existing logo and business card. The final design should communicate a sense of luxury, but also be fun and oriented towards children.
Our current website is www.mavoret.com. Note: Not all products are loaded.
Changes to the color scheme, fonts, background and graphics are welcome. And while we like the layout of my current TrellaCart theme (Seashore), we do expect that SMALL modifications will be needed to make it ours. For example, we would like the cart to be placed more visibly. I have a designer that can code the changes you come up with so feel free to suggest what you feel is best.
We look forward to your designs. Good luck!
Websites we like:
https://www.shopwrenfig.com/ (The layout of this site is nice to me)
http://www.elsiesattic.com/
http://www.quietmeadowherbals.com/
Updates
This contest is for PSD design only. No Trellacart development or coding is required.
Target Market(s)
Our typical customer is female age 20-45 shopping for her own child or for a gift.
Industry/Entity Type
Boutique
Requirements
Must have
- PSD Design
- These 5 items listed below are things we’d like:
- (1) General styling (color scheme, fonts, background, graphics, etc.) & layout
- • ONLY the logo colors are set … feel free to add colors that compliment it
- • Prefer narrow (or single line) footer
- • We think the main banner/image is too large
- (2) Create main banner/image (current template uses 970px wide)
- (3) AT LEAST Three (3) Marketing banners (current template uses 433 x 225):
- • Our Hottest Products
- • Our Newest Arrivals
- • Newsletter sign-up
- (4) Border to enclose admin links (My account, Gift Certificates, Create an Account)
- (5) New badges / icon / images
- • Shopping Cart --> Bag or cart image should stand out; try to place above search bar (you’ll have to lower the search bar to do this)
- • Sale Badge --> anything goes. Could be a badge or a sash. Might also be nice to have these for the bestsellers as well.
- • Star Icons for product reviews (optional) --> Keep the stars just have them be more stylized
Nice to have
- We like pages that have a background and think one might look good on our site if not too busy.
Should not have
- We do not like extremely dark backgrounds for web pages.

```html
<!DOCTYPE html>
<html lang="en">
<head>
<meta charset="utf-8">
<title>Mavoret Childrenswear</title>
<link href="https://fonts.googleapis.com/css2?family=Open+Sans:ital,wght@0,400;0,600;0,700;1,400&family=Roboto+Condensed:wght@400&family=Playfair+Display:ital,wght@0,400;1,400&family=Libre+Baskerville:ital@0;1&display=swap" rel="stylesheet">
<style>
:root{
  --lilac:#e6d4e6;
  --teal:#2a8b8b;
  --teal-dark:#1f7c7e;
  --sky:#d3edf4;
  --sky-edge:#9fd3e3;
  --aqua:#bdeee9;
  --cream:#fdf9e6;
  --cream-ink:#8b6b33;
  --orange:#e8692c;
  --red:#e0312b;
  --yellow:#ffe000;
  --ink:#1e1e1e;
  --grey:#8d8d8d;
  --white:#ffffff;
}
*{box-sizing:border-box;margin:0;padding:0}
html,body{width:1179px;height:1200px;overflow:hidden;background:var(--lilac)}
.stage{position:absolute;left:0;top:0;width:1200px;height:1221px;transform:scale(.9825);transform-origin:0 0;font-family:"Open Sans",sans-serif;color:var(--ink)}
.abs{position:absolute}
.sheet{left:115px;top:65px;width:975px;height:1095px;background:var(--white);border-radius:6px;box-shadow:0 0 0 3px rgba(255,255,255,.6)}
.brand{left:145px;top:95px;display:flex;align-items:center;gap:14px}
.brand-dot{width:60px;height:60px;border-radius:50%;background:#cdeeee}
.brand-name{font-family:"Playfair Display",serif;font-size:52px;color:var(--teal);letter-spacing:1px}
.account-links{left:678px;top:102px;display:flex;gap:24px;font-size:13px;color:var(--teal)}
.account-links span{display:flex;align-items:center;gap:6px}
.callout{left:719px;top:157px;font-size:15px;color:var(--grey)}
.callout b{font-weight:400;color:var(--teal)}
.cart-button{left:945px;top:152px;width:109px;height:32px;border-radius:6px;background:#e2e2e2;display:flex;overflow:hidden}
.cart-button .icon{width:46px;background:var(--yellow);display:flex;align-items:center;justify-content:center}
.cart-button .count{font-size:13px;font-weight:600;line-height:32px;padding-left:8px}
.ribbon{left:70px;top:228px;width:1065px;height:60px}
.main-nav{left:0;top:244px;width:1200px;height:20px;font-style:italic;font-size:14px;color:var(--teal-dark);text-transform:uppercase}
.main-nav span{position:absolute;top:0;white-space:nowrap}
.search{left:879px;top:240px;width:196px;height:27px;background:var(--white);border-radius:4px;font-size:11px;color:var(--grey);padding:6px 12px}
.search svg{position:absolute;right:8px;top:5px}
.shop-menu{left:135px;top:290px;width:183px;height:285px;background:var(--cream);border-radius:40px 40px 50px 50px;border:1px solid #efe7c6;text-align:center;font-family:"Roboto Condensed",sans-serif;font-size:13px;color:var(--cream-ink)}
.shop-menu h3{font-family:"Libre Baskerville",serif;font-style:italic;font-weight:400;font-size:18px;color:#cbbd95;margin:16px 0 10px}
.shop-menu li{list-style:none;line-height:24.3px}
.hero{left:355px;top:290px;width:720px;height:271px;border-radius:4px;background:linear-gradient(90deg,#d9c0ae 0%,#eedbd6 40%,#f6e6ea 70%,#f7eef2 100%)}
.hero-big{left:814px;top:299px;font-family:"Playfair Display",serif;font-size:130px;line-height:130px;font-variant-numeric:lining-nums;font-feature-settings:"lnum" 1;white-space:nowrap}
.hero-off{left:918px;top:344px;font-family:"Libre Baskerville",serif;font-style:italic;font-size:28px;line-height:36px;white-space:nowrap}
.hero-tag{left:740px;top:429px;width:280px;text-align:center;font-family:"Libre Baskerville",serif;font-style:italic;font-size:16px;line-height:22px;white-space:nowrap}
.hero-name{left:740px;top:451px;width:280px;text-align:center;font-family:"Playfair Display",serif;font-size:50px;line-height:56px;color:var(--teal);letter-spacing:2px;white-space:nowrap}
.cart-widget{left:140px;top:612px;width:170px;height:98px;background:#a8dbe6;border-radius:14px;border:3px solid #cdeff5;text-align:center}
.cart-widget h4{font-family:"Libre Baskerville",serif;font-style:italic;font-weight:400;font-size:15px;color:var(--teal-dark);margin-top:10px}
.cart-widget p{font-size:11px;color:var(--teal-dark);margin-top:4px}
.cart-widget .go{display:inline-block;margin-top:6px;background:var(--white);border-radius:10px;padding:1px 12px;font-family:"Libre Baskerville",serif;font-style:italic;font-size:12px;color:var(--teal-dark)}
.promo{height:129px;top:578px}
.promo .photo{position:absolute;top:0;height:100%}
.promo .title{position:absolute;font-family:"Libre Baskerville",serif;font-style:italic;font-size:21px;line-height:1}
.promo .sub{position:absolute;font-family:"Libre Baskerville",serif;font-style:italic;font-size:16px;color:var(--grey)}
.promo .cta{position:absolute;font-size:12.5px;color:var(--red)}
.hot{left:355px;width:235px;background:var(--white)}
.new{left:606px;width:224px;background:#fbf3b0}
.newsletter{left:851px;top:578px;width:224px;height:129px;background:var(--aqua)}
.newsletter h4{position:absolute;left:8px;top:11px;font-size:16px;font-weight:600;color:var(--teal-dark)}
.newsletter .more{position:absolute;left:8px;top:35px;font-size:12px;font-weight:600}
.newsletter .field{position:absolute;left:7px;top:60px;width:206px;height:24px;background:var(--white);font-size:12px;padding:4px 7px;color:#333}
.newsletter .arrow{position:absolute;right:0;top:0;width:20px;height:24px;background:#8f8f8f}
.newsletter .login{position:absolute;left:5px;top:93px;width:86px;height:23px;background:var(--yellow);font-size:14px;font-weight:600;padding-left:24px;line-height:23px}
.featured-title{left:138px;top:740px;font-family:"Playfair Display",serif;font-size:26px;color:var(--teal);letter-spacing:1px}
.featured-title em{font-style:normal;color:var(--orange)}
.rule{left:138px;top:777px;width:930px;border-top:2px dashed #dedede}
.product{top:800px;width:150px;text-align:center}
.product .pic{margin:0 auto;width:110px;height:130px;border-radius:10px;background:linear-gradient(180deg,#f4f4f4,#dcdcdc)}
.product .name{font-size:13px;margin-top:18px}
.product .price{font-size:17px;color:var(--orange);margin-top:2px}
.sale{left:304px;top:804px;width:50px;height:24px;background:var(--orange);color:var(--white);font-size:11.5px;line-height:24px;text-align:center;border-radius:4px 4px 0 4px}
.stars{left:183px;top:1003px;display:flex;gap:1px}
.details{left:168px;top:1030px;width:109px;height:34px;border-radius:6px;background:#ececec;display:flex;overflow:hidden}
.details .icon{width:46px;background:var(--yellow);display:flex;align-items:center;justify-content:center}
.details span{font-size:13px;font-weight:600;line-height:34px;padding-left:8px}
.footer{left:115px;top:1104px;width:975px;height:56px;background:var(--sky);border-top:4px dotted #a9a4c8;text-align:center;font-size:15px;line-height:48px;border-radius:0 0 6px 6px}
</style>
</head>
<body>
<div class="stage">
  <div class="abs sheet"></div>

  <div class="abs brand"><div class="brand-dot"></div><div class="brand-name">Mavoret</div></div>

  <div class="abs account-links">
    <span><svg width="14" height="16" viewBox="0 0 14 16"><circle cx="7" cy="4.5" r="4" fill="#2a8b8b"/><path d="M0 16c0-5 3-7 7-7s7 2 7 7z" fill="#2a8b8b"/></svg>My Account</span>
    <span><svg width="13" height="16" viewBox="0 0 13 16"><rect x="1" y="1" width="10" height="14" fill="none" stroke="#2a8b8b" stroke-width="2"/><path d="M3 5h6M3 8h6" stroke="#2a8b8b"/></svg>Gift Certificates</span>
    <span><svg width="15" height="15" viewBox="0 0 15 15"><rect width="15" height="15" fill="#2a8b8b"/><path d="M7.5 3v9M3 7.5h9" stroke="#fff" stroke-width="2"/></svg>Create An Account</span>
  </div>
  <div class="abs callout">Call us toll free: <b>(555) 214 -730</b></div>
  <div class="abs cart-button">
    <div class="icon"><svg width="22" height="20" viewBox="0 0 22 20"><path d="M0 1h4l3 11h12l2-8H6" fill="none" stroke="#111" stroke-width="2.4"/><circle cx="8" cy="17" r="2" fill="#111"/><circle cx="17" cy="17" r="2" fill="#111"/></svg></div>
    <div class="count">0 items</div>
  </div>

  <svg class="abs ribbon" viewBox="0 0 1065 60">
    <path d="M0 4h40l-14 26 14 28H10l6-26z" fill="#b9e1ee"/>
    <path d="M1065 4h-40l14 26-14 28h30l-6-26z" fill="#b9e1ee"/>
    <rect x="22" y="2" width="1021" height="44" fill="#d3edf4"/>
    <line x1="22" y1="46" x2="1043" y2="46" stroke="#9fd3e3" stroke-width="2"/>
  </svg>
  <nav class="abs main-nav">
    <span style="left:163px">New Baby</span>
    <span style="left:279px">Christening &amp; Baptisim</span>
    <span style="left:497px">Birthday</span>
    <span style="left:614px">Holiday</span>
    <span style="left:727px">Wedding</span>
  </nav>
  <div class="abs search">Search..<svg width="18" height="18" viewBox="0 0 18 18"><circle cx="7" cy="7" r="6" fill="none" stroke="#999" stroke-width="1.6"/><path d="M11.5 11.5l5 5" stroke="#999" stroke-width="1.8"/></svg></div>

  <div class="abs shop-menu">
    <h3>shop</h3>
    <ul><li>New Baby Care</li><li>Birthday</li><li>Christening &amp; Baptiisim</li><li>Wedding</li><li>For the Boys</li><li>For the Girls</li><li>Every Clothing</li><li>New babies</li></ul>
  </div>

  <div class="abs hero" role="img" aria-label="Photo of a baby in a knitted pink hat lying on a soft pink blanket"></div>
  <div class="abs hero-big">30</div>
  <div class="abs hero-off">% off</div>
  <div class="abs hero-tag">Special occasion Bips &amp; Pieces</div>
  <div class="abs hero-name">MAVORET</div>

  <div class="abs cart-widget">
    <h4>Your cart</h4>
    <p>$ 0.00 for 0 items</p>
    <span class="go">checkout</span>
  </div>

  <div class="abs promo hot">
    <div class="photo" role="img" aria-label="Photo of a sitting baby in a yellow outfit" style="left:5px;width:135px;background:linear-gradient(180deg,#f6e2cc,#f2e48a)"></div>
    <div class="title" style="left:150px;top:27px">Hotest</div>
    <div class="sub" style="left:146px;top:50px">Arrival</div>
    <div class="cta" style="left:144px;top:72px">SHOP NOW</div>
  </div>
  <div class="abs promo new">
    <div class="photo" role="img" aria-label="Photo of a smiling baby" style="left:0;width:110px;background:linear-gradient(90deg,#f1cfb3,#fbf3b0)"></div>
    <div class="title" style="left:144px;top:34px">New</div>
    <div class="sub" style="left:140px;top:58px">Arrival</div>
    <div class="cta" style="left:139px;top:81px">SHOP NOW</div>
  </div>
  <div class="abs newsletter">
    <h4>Get Our Newsletter</h4>
    <div class="more">More Info&gt;&gt;</div>
    <div class="field">SIgn up Now!<div class="arrow"><svg width="20" height="24" viewBox="0 0 20 24"><path d="M8 7l5 5-5 5" fill="none" stroke="#fff" stroke-width="2"/></svg></div></div>
    <div class="login">Login</div>
  </div>

  <div class="abs featured-title">FEATURED <em>PRODUCTS</em></div>
  <div class="abs rule"></div>

  <div class="abs product" style="left:138px"><div class="pic" role="img" aria-label="White organza baby booties"></div><div class="name">Organza bootie white</div><div class="price">$ 85</div></div>
  <div class="abs product" style="left:300px"><div class="pic" role="img" aria-label="White christening bib"></div><div class="name">Bib White</div><div class="price">$ 35</div></div>
  <div class="abs product" style="left:458px"><div class="pic" role="img" aria-label="White lace-up baby shoes"></div><div class="name">Lace Trim White</div><div class="price">$ 35</div></div>
  <div class="abs product" style="left:623px"><div class="pic" role="img" aria-label="Round satin bib with lace trim"></div><div class="name">Satin West Short</div><div class="price">$ 35</div></div>
  <div class="abs product" style="left:783px"><div class="pic" role="img" aria-label="White christening bib"></div><div class="name">Bib White</div><div class="price">$ 35</div></div>
  <div class="abs product" style="left:947px"><div class="pic" role="img" aria-label="White satin boys' short set with hat"></div><div class="name">Satin West Short</div><div class="price">$ 35</div></div>
  <div class="abs sale">SALE</div>

  <div class="abs stars">
    <svg width="74" height="14" viewBox="0 0 74 14"><g fill="#f7b500"><path id="st" d="M7 0l2 4.6 5 .4-3.8 3.3 1.2 4.9L7 10.5 2.6 13.2l1.2-4.9L0 5l5-.4z"/><use href="#st" x="15"/><use href="#st" x="30"/><use href="#st" x="45"/><use href="#st" x="60"/></g></svg>
  </div>
  <div class="abs details">
    <div class="icon"><svg width="22" height="20" viewBox="0 0 22 20"><path d="M0 1h4l3 11h12l2-8H6" fill="none" stroke="#111" stroke-width="2.4"/><circle cx="8" cy="17" r="2" fill="#111"/><circle cx="17" cy="17" r="2" fill="#111"/></svg></div>
    <span>Details</span>
  </div>

  <footer class="abs footer">Copyright©Mavoret.com All Right Reserved</footer>
</div>
</body>
</html>
```